Pretty up existing catalogue

Catalog available - should simply be made new / fresh - ideally in corel draw? Please use page 14 as a sample design! Many thanks. Otherwise you can let off steam completely in terms of design. Thanks

Target Market(s)

customers worldwide

Industry/Entity Type

Bau

Font styles to use
Serif
Sans Serif

Requirements
Must have
• Logo must remain the same, modern look
Nice to have
• fresh modern look
Should not have
• extreme colors, log change

```html
<!DOCTYPE html>
<html lang="de">
<head>
<meta charset="utf-8">
<title>Haltenadeln – Katalogseite 14</title>
<link href="https://fonts.googleapis.com/css2?family=Montserrat:wght@400;500;700;800&display=swap" rel="stylesheet">
<style>
  :root {
    --cream: #f8f7dd;
    --yellow: #f1e216;
    --card: #4d4d4d;
    --card-edge: #3b3b3b;
    --ink: #3f3f3f;
    --white: #ffffff;
    --accent: #f1e216;
  }
  * { margin: 0; padding: 0; box-sizing: border-box; }
  html, body { width: 927px; height: 1200px; overflow: hidden; }
  body {
    background: var(--cream);
    font-family: "Montserrat", sans-serif;
    color: var(--ink);
    position: relative;
  }
  .page-header { position: absolute; left: 68px; top: 52px; }
  .page-title {
    font-weight: 800;
    font-size: 50px;
    letter-spacing: 0.5px;
    color: var(--ink);
    line-height: 1;
  }
  .page-intro {
    margin-top: 33px;
    font-size: 20.4px;
    font-weight: 400;
    line-height: 28.5px;
    color: #222;
    width: 715px;
  }
  .product-band {
    position: absolute;
    left: 0; top: 227px;
    width: 927px; height: 888px;
    background: var(--yellow);
    padding: 71px 0 0 63px;
  }
  .product-grid {
    display: grid;
    grid-template-columns: 391px 391px;
    grid-auto-rows: 164px;
    column-gap: 20px;
    row-gap: 34px;
  }
  .product-card {
    background: var(--card);
    border: 2px solid var(--card-edge);
    display: flex;
    align-items: stretch;
    padding: 2px 0 2px 4px;
  }
  .product-image {
    width: 143px;
    flex: none;
  }
  .product-info {
    padding: 0 2px 0 22px;
    display: flex;
    flex-direction: column;
    justify-content: center;
    color: var(--white);
    font-size: 12.1px;
    line-height: 14.6px;
    font-weight: 500;
    white-space: nowrap;
  }
  .product-name {
    color: var(--accent);
    font-weight: 800;
    font-size: 15.5px;
    line-height: 18px;
    margin-bottom: 11px;
  }
  .label { color: var(--accent); font-weight: 700; }
  .page-number {
    position: absolute;
    left: 0; width: 900px; top: 1148px;
    text-align: center;
    font-size: 17px;
    color: #222;
  }
</style>
</head>
<body>
  <header class="page-header">
    <h1 class="page-title">HALTENADELN</h1>
    <p class="page-intro">Zur Befestigung von Kestler Schienen, Folien und Rohrbögen auf Isolation</p>
  </header>

  <section class="product-band">
    <div class="product-grid">
      <article class="product-card">
        <div class="product-image" role="img" aria-label="Blaue Haltenadel mit Widerhaken" style="background: radial-gradient(circle at 50% 45%, #8a94d8 0%, #ffffff 62%);"></div>
        <div class="product-info">
          <h2 class="product-name">Artikel Nr. 4120</h2>
          <span class="label">Länge: 39 mm</span>
          <span>Fur Rohre mit einem ø bis 20 mm</span>
          <span>Per Hand zu setzen</span>
          <span class="label">Verpackung:</span>
          <span>500 stück/Beutel</span>
          <span>5.000 stuck/Karton</span>
        </div>
      </article>

      <article class="product-card">
        <div class="product-image" role="img" aria-label="Rote Haltenadel mit Widerhaken" style="background: radial-gradient(circle at 50% 45%, #f08a8a 0%, #ffffff 62%);"></div>
        <div class="product-info">
          <h2 class="product-name">Artikel Nr. KHN40</h2>
          <span class="label">Länge: 39 mm</span>
          <span>Für Rohre mit einem ø bis 20 mm</span>
          <span>Mit KestPin zu setzen</span>
          <span class="label">Verpackung:</span>
          <span>250 stück/Karton</span>
          <span>Magaziniert á 25 Stück</span>
        </div>
      </article>

      <article class="product-card">
        <div class="product-image" role="img" aria-label="Grüne Haltenadel mit Widerhaken" style="background: radial-gradient(circle at 50% 45%, #7fbf8a 0%, #ffffff 62%);"></div>
        <div class="product-info">
          <h2 class="product-name">Artikel Nr. KHN50</h2>
          <span class="label">Länge: 39 mm</span>
          <span>Fur Rohre mit einem ø bis 20 mm</span>
          <span>Per Hand zu setzen</span>
          <span class="label">Verpackung:</span>
          <span>500 stück/Beutel</span>
          <span>5.000 stuck/Karton</span>
        </div>
      </article>

      <article class="product-card">
        <div class="product-image" role="img" aria-label="Schwarze Haltenadel mit Widerhaken" style="background: radial-gradient(circle at 50% 45%, #9a9a9a 0%, #ffffff 62%);"></div>
        <div class="product-info">
          <h2 class="product-name">Artikel Nr. 4120</h2>
          <span class="label">Länge: 52 mm</span>
          <span>Fur Rohre mit einem ø bis 26 mm</span>
          <span>Per Hand zu setzen</span>
          <span class="label">Verpackung:</span>
          <span>100 stück/Beutel</span>
          <span>1.000 stuck/Karton</span>
        </div>
      </article>

      <article class="product-card">
        <div class="product-image" role="img" aria-label="Blaue U-förmige Haltenadel" style="background: radial-gradient(circle at 50% 45%, #8f92cf 0%, #ffffff 62%);"></div>
        <div class="product-info">
          <h2 class="product-name">Artikel Nr. KHN40</h2>
          <span class="label">Länge: 39 mm</span>
          <span>Für Rohre mit einem ø bis 20 mm</span>
          <span>Mit KestPin zu setzen</span>
          <span><span class="label">Verpackung</span>:</span>
          <span>250 stück/Karton</span>
          <span>Magaziniert á 25 Stück</span>
        </div>
      </article>

      <article class="product-card">
        <div class="product-image" role="img" aria-label="Orange U-förmige Haltenadel" style="background: radial-gradient(circle at 50% 45%, #f5a27f 0%, #ffffff 62%);"></div>
        <div class="product-info">
          <h2 class="product-name">Artikel Nr. KHN50</h2>
          <span class="label">Länge: 47 mm</span>
          <span>Fur Rohre mit einem ø bis 20 mm</span>
          <span>Mit KestPin zu setzen</span>
          <span><span class="label">Verpackung</span>:</span>
          <span>250 stück/Beutel</span>
          <span>Magaziniert a 25 Stück</span>
        </div>
      </article>

      <article class="product-card">
        <div class="product-image" role="img" aria-label="Grüne U-förmige Haltenadel" style="background: radial-gradient(circle at 50% 45%, #8fd69a 0%, #ffffff 62%);"></div>
        <div class="product-info">
          <h2 class="product-name">Artikel Nr. KHN60</h2>
          <span class="label">Länge: 62 mm</span>
          <span>Für Rohre mit einem ø bis 20 mm</span>
          <span>Mit KestPin zu setzen</span>
          <span><span class="label">Verpackung</span>:</span>
          <span>250 stück/Karton</span>
          <span>Magaziniert á 25 Stück</span>
        </div>
      </article>

      <article class="product-card">
        <div class="product-image" role="img" aria-label="Setzgerät für Haltenadeln" style="background: radial-gradient(circle at 50% 50%, #c9c9c9 0%, #ffffff 60%);"></div>
        <div class="product-info">
          <h2 class="product-name">KestPin</h2>
          <span class="label">Artikel Nr. KSG</span>
          <span>Setzgerät für Haltenadeln KHN40,</span>
          <span>KHN50 imd</span>
          <span class="label">Verpackung:</span>
          <span>1 Stück / Karton</span>
        </div>
      </article>
    </div>
  </section>

  <footer class="page-number">14</footer>
</body>
</html>
```